Interactive Report Dashboard for Data Analytics

Please see this google doc for information and pictures regarding our project.
https://files.plomvex.com/doc/8TrwQ2mZpLx4VnKc0sYd7HjE3fRb9uNa5Gq/view?share=open
Feel free to message me if you have any questions.
Target Market(s)
This is for video producers, youtubers, and online teachers.
We run focus groups for them and help them understand how their audience reacts to the video content.
Coding
Coded - Design and coding required
Number of Pages Required
5+ page
Colors
Designer to choose colors to be used in the design.
Look and feel
Each slider illustrates characteristics of the customer's brand and the style your logo design should communicate.

```html
<!DOCTYPE html>
<html lang="en">
<head>
<meta charset="utf-8">
<title>Vidlume – Audience Analytic Tools</title>
<link rel="stylesheet" href="https://fonts.googleapis.com/css2?family=Montserrat:wght@400;500;600;700;800&display=swap">
<style>
:root{
  --header-bg:#2b2f36;
  --search-bg:#3c4149;
  --white:#ffffff;
  --ink:#25282d;
  --ink-soft:#4a4e55;
  --muted:#9da1a7;
  --line:#d9dbde;
  --line-soft:#e8e9eb;
  --tab-active:#a9adb2;
  --control:#dfe1e4;
  --pill:#9ea2a7;
  --alert:#f2b01e;
  --chart-blue:#3366cc;
  --chart-red:#dc3912;
  --chart-orange:#ff9900;
  --chart-green:#109618;
  --chart-purple:#990099;
  --map-green:#3f9f3a;
}
*{box-sizing:border-box;margin:0;padding:0}
html,body{width:1200px;height:859px;overflow:hidden;background:var(--white)}
body{font-family:"Montserrat",Arial,sans-serif;color:var(--ink);position:relative}

/* header */
.app-header{position:absolute;left:0;top:0;width:1200px;height:73px;background:var(--header-bg)}
.brand{position:absolute;left:49px;top:19px;font-size:27px;font-weight:800;color:var(--white);letter-spacing:.5px}
.search{position:absolute;left:277px;top:19px;width:414px;height:36px;border-radius:18px;background:var(--search-bg)}
.search svg{position:absolute;right:14px;top:9px}
.header-icon{position:absolute;top:25px}
.avatar{position:absolute;left:905px;top:18px;width:37px;height:37px;border-radius:50%;background:radial-gradient(circle at 50% 40%,#e0b79a,#8a5a3e)}
.user-name{position:absolute;left:969px;top:28px;font-size:14px;font-weight:600;color:var(--white)}

/* tabs */
.tabs{position:absolute;left:0;top:73px;width:1200px;height:38px;display:flex;border-bottom:1px solid var(--line-soft)}
.tab{flex:1;display:flex;align-items:center;justify-content:center;font-size:12px;font-weight:700;letter-spacing:.8px;color:#b6b9bd;border-left:1px solid var(--line-soft)}
.tab.is-active{background:var(--tab-active);color:var(--ink);border-left:none;position:relative}
.tab.is-active::after{content:"";position:absolute;left:190px;bottom:-9px;border:9px solid transparent;border-top-color:var(--tab-active);border-bottom:0}

/* filters */
.filters{position:absolute;left:0;top:139px;width:231px;height:720px;border-right:2px solid var(--line-soft)}
.filters-title{position:absolute;left:47px;top:28px;font-size:18px;font-weight:700}
.filter-label{position:absolute;left:47px;font-size:14px;font-weight:500;color:var(--ink-soft)}
.range{position:absolute;left:47px;width:137px;height:40px}
.range-track{position:absolute;left:0;right:0;bottom:2px;height:2px;background:var(--line)}
.range-knob{position:absolute;bottom:0;width:6px;height:6px;border-radius:50%;background:var(--muted)}
.range-pill{position:absolute;top:0;height:21px;padding:0 9px;border-radius:11px;background:var(--pill);font-size:11px;font-weight:600;line-height:21px;color:var(--ink)}
.range-pill::after{content:"";position:absolute;left:50%;bottom:-5px;margin-left:-5px;border:5px solid transparent;border-top-color:var(--pill);border-bottom:0}
.select{position:absolute;left:47px;width:137px;height:37px;background:var(--control)}
.select svg{position:absolute;right:12px;top:15px}

/* content */
.sort{position:absolute;left:277px;top:157px;width:276px;height:36px;border:2px solid var(--line);font-size:14px;font-weight:500;padding:8px 0 0 15px;color:var(--ink-soft)}
.sort svg{position:absolute;right:14px;top:13px}
.view-toggle{position:absolute;top:157px;width:36px;height:36px;border-radius:50%;border:2px solid var(--line);display:flex;align-items:center;justify-content:center}
.view-toggle.is-active{background:#a4a8ad;border-color:#a4a8ad}
.scroll-track{position:absolute;left:1180px;top:139px;width:6px;height:688px;border-radius:3px;background:#eeeff0}
.scroll-thumb{position:absolute;left:1180px;top:213px;width:6px;height:140px;border-radius:3px;background:#c9cbce}

.card{position:absolute;width:273px}
.card-stack{position:relative;width:273px;height:189px}
.card-stack::before,.card-stack::after{content:"";position:absolute;border:1px solid var(--line);background:var(--white)}
.card-stack::after{left:8px;top:-4px;right:-8px;bottom:4px}
.card-stack::before{left:4px;top:-2px;right:-4px;bottom:2px;z-index:1}
.card-face{position:absolute;inset:0;border:1px solid var(--line);background:var(--white);z-index:2;overflow:hidden}
.card-title{margin-top:18px;font-size:14.5px;font-weight:700;letter-spacing:.4px}
.card-meta{margin-top:8px;font-size:10.5px;font-weight:600;letter-spacing:1.2px;color:var(--ink-soft);display:flex;align-items:center;gap:12px}
.card-meta svg{vertical-align:-1px;margin-right:3px}
.map-fill{position:absolute;left:22px;top:8px;width:245px;height:166px;background:linear-gradient(110deg,#e6e6e6 0%,#9cd08f 30%,#e2e2e2 55%,var(--map-green) 85%);border-radius:4px}
.chart text{font-family:"Montserrat",Arial,sans-serif}
</style>
</head>
<body>

<header class="app-header">
  <div class="brand">Vidlume</div>
  <div class="search">
    <svg width="18" height="18" viewBox="0 0 18 18" fill="none" stroke="#c6c9cd" stroke-width="1.8"><circle cx="10" cy="7.5" r="5.5"/><path d="M6 11.5 1.5 16"/></svg>
  </div>
  <svg class="header-icon" style="left:738px;top:22px" width="22" height="24" viewBox="0 0 22 24" fill="none" stroke="#c6c9cd" stroke-width="1.8"><path d="M4 17V10a6 6 0 0 1 12 0v7l2 2H2z"/><path d="M8 21h4"/><circle cx="17" cy="4" r="3.5" fill="var(--alert)" stroke="none"/></svg>
  <svg class="header-icon" style="left:787px" width="21" height="20" viewBox="0 0 24 23" fill="#c6c9cd"><path d="m12 1 3.3 7 7.7.9-5.7 5.3 1.5 7.6L12 18l-6.8 3.8 1.5-7.6L1 8.9 8.7 8z"/></svg>
  <svg class="header-icon" style="left:838px" width="21" height="21" viewBox="0 0 22 22" fill="none" stroke="#c6c9cd" stroke-width="1.8"><circle cx="11" cy="11" r="9"/><path d="M11 10v6M11 6.5v.5"/></svg>
  <div class="avatar" role="img" aria-label="User profile photo"></div>
  <div class="user-name">Mara Ellison</div>
  <svg class="header-icon" style="left:1131px;top:26px" width="20" height="20" viewBox="0 0 20 20" fill="none" stroke="#c6c9cd" stroke-width="1.8"><circle cx="10" cy="10" r="3"/><circle cx="10" cy="10" r="7.5" stroke-width="3" stroke-dasharray="3 2.9"/></svg>
</header>

<nav class="tabs">
  <div class="tab is-active">AUDIENCE ANALYTIC TOOLS</div>
  <div class="tab">REAL TIME EMOTION DISPLAY</div>
  <div class="tab">SURVEY RESPONSES</div>
</nav>

<aside class="filters">
  <div class="filters-title">Filters by</div>

  <div class="filter-label" style="top:62px">Age</div>
  <div class="range" style="top:93px">
    <div class="range-pill" style="left:0">17</div>
    <div class="range-pill" style="left:83px">64</div>
    <div class="range-track"></div>
    <div class="range-knob" style="left:17px"></div>
    <div class="range-knob" style="left:100px"></div>
  </div>

  <div class="filter-label" style="top:155px">Income</div>
  <div class="range" style="top:185px">
    <div class="range-pill" style="left:0">9.9K</div>
    <div class="range-pill" style="left:76px">115.8K</div>
    <div class="range-track"></div>
    <div class="range-knob" style="left:20px"></div>
    <div class="range-knob" style="left:108px"></div>
  </div>

  <div class="filter-label" style="top:248px">Nationality</div>
  <div class="select" style="top:270px"><svg width="10" height="6" viewBox="0 0 10 6" fill="none" stroke="#8d9197" stroke-width="1.5"><path d="m1 1 4 4 4-4"/></svg></div>
  <div class="filter-label" style="top:325px">Education</div>
  <div class="select" style="top:348px"><svg width="10" height="6" viewBox="0 0 10 6" fill="none" stroke="#8d9197" stroke-width="1.5"><path d="m1 1 4 4 4-4"/></svg></div>
  <div class="filter-label" style="top:402px">Gender</div>
  <div class="select" style="top:425px"><svg width="10" height="6" viewBox="0 0 10 6" fill="none" stroke="#8d9197" stroke-width="1.5"><path d="m1 1 4 4 4-4"/></svg></div>
  <div class="filter-label" style="top:480px">Interests</div>
  <div class="select" style="top:502px"><svg width="10" height="6" viewBox="0 0 10 6" fill="none" stroke="#8d9197" stroke-width="1.5"><path d="m1 1 4 4 4-4"/></svg></div>
  <div class="filter-label" style="top:557px">Personality</div>
  <div class="select" style="top:580px"><svg width="10" height="6" viewBox="0 0 10 6" fill="none" stroke="#8d9197" stroke-width="1.5"><path d="m1 1 4 4 4-4"/></svg></div>
</aside>

<main>
  <div class="sort">Sort by<svg width="10" height="6" viewBox="0 0 10 6" fill="none" stroke="#8d9197" stroke-width="1.5"><path d="m1 1 4 4 4-4"/></svg></div>
  <div class="view-toggle is-active" style="left:1071px"><svg width="16" height="16" viewBox="0 0 16 16" fill="none" stroke="#fff" stroke-width="1.6"><rect x="1" y="1" width="14" height="14"/><path d="M8 1v14M1 8h14"/></svg></div>
  <div class="view-toggle" style="left:1117px"><svg width="16" height="14" viewBox="0 0 16 14" fill="none" stroke="#a4a8ad" stroke-width="1.4"><rect x="1" y="1" width="14" height="12"/><path d="M1 5h14M1 9h14M5 1v12"/></svg></div>
  <div class="scroll-track"></div>
  <div class="scroll-thumb"></div>

  <!-- row 1 -->
  <article class="card" style="left:277px;top:240px">
    <div class="card-stack"><div class="card-face"><div class="map-fill" role="img" aria-label="World map shading regions by audience size in greens"></div></div></div>
    <h3 class="card-title">Region GeoCharts Lorem Ipsum</h3>
    <div class="card-meta"><span>12 VIEW</span><span>I</span><span><svg width="10" height="10" viewBox="0 0 24 23" fill="none" stroke="#4a4e55" stroke-width="2.5"><path d="m12 1 3.3 7 7.7.9-5.7 5.3 1.5 7.6L12 18l-6.8 3.8 1.5-7.6L1 8.9 8.7 8z"/></svg>4.5</span></div>
  </article>

  <article class="card" style="left:577px;top:240px">
    <div class="card-stack"><div class="card-face">
      <svg class="chart" width="273" height="189" viewBox="0 0 273 189">
        <text x="42" y="30" font-size="5.5" fill="#222">Age vs. Weight comparison</text>
        <g stroke="#e3e3e3" stroke-width=".7">
          <path d="M43 37h189M43 64h189M43 91h189M43 118h189M90 37v107M138 37v107M185 37v107M232 37v107"/>
        </g>
        <path d="M43 37v107h189" fill="none" stroke="#999" stroke-width=".8"/>
        <g fill="var(--chart-blue)">
          <circle cx="75" cy="119" r="1.6"/><circle cx="84" cy="113" r="1.6"/><circle cx="84" cy="110" r="1.6"/>
          <circle cx="105" cy="102" r="1.6"/><circle cx="119" cy="77" r="1.6"/><circle cx="147" cy="68" r="1.6"/>
        </g>
        <g font-size="4.5" fill="#666">
          <text x="37" y="40">20</text><text x="37" y="67">15</text><text x="37" y="94">10</text><text x="39" y="121">5</text>
          <text x="88" y="151">5</text><text x="135" y="151">10</text><text x="182" y="151">15</text><text x="229" y="151">20</text>
          <text x="130" y="160">Age</text><text x="28" y="96" transform="rotate(-90 28 96)">Weight</text>
        </g>
      </svg>
    </div></div>
    <h3 class="card-title">Visualization: Scatter Chart</h3>
    <div class="card-meta"><span>12 VIEW</span><span>I</span><span><svg width="10" height="10" viewBox="0 0 24 23" fill="none" stroke="#4a4e55" stroke-width="2.5"><path d="m12 1 3.3 7 7.7.9-5.7 5.3 1.5 7.6L12 18l-6.8 3.8 1.5-7.6L1 8.9 8.7 8z"/></svg>4.5</span></div>
  </article>

  <article class="card" style="left:877px;top:240px">
    <div class="card-stack"><div class="card-face">
      <svg class="chart" width="273" height="189" viewBox="0 0 273 189">
        <text x="33" y="40" font-size="5.5" fill="#222">Lengths of dinosaurs, in meters</text>
        <g stroke="#e3e3e3" stroke-width=".7"><path d="M33 63h207M33 85h207M33 107h207M33 129h207"/></g>
        <g fill="var(--chart-blue)" stroke="#fff" stroke-width=".6">
          <rect x="33" y="63" width="41" height="88"/><rect x="74" y="127" width="41" height="24"/>
          <rect x="115" y="132" width="41" height="19"/><rect x="156" y="127" width="41" height="24"/>
          <rect x="197" y="144" width="41" height="7"/>
          <path d="M33 70h41M33 77h41M33 84h41M33 91h41M33 98h41M33 105h41M33 112h41M33 119h41M33 126h41M33 133h41M33 140h41M74 134h41M74 141h41M115 139h41M156 134h41M156 141h41"/>
        </g>
        <path d="M33 151h207" stroke="#999" stroke-width=".8"/>
        <g font-size="4.5" fill="#666"><text x="31" y="159">0</text><text x="72" y="159">10</text><text x="113" y="159">20</text><text x="154" y="159">30</text><text x="195" y="159">40</text><text x="236" y="159">50</text></g>
      </svg>
    </div></div>
    <h3 class="card-title">Histogram Lorem Ipsum</h3>
    <div class="card-meta"><span>12 VIEW</span><span>I</span><span><svg width="10" height="10" viewBox="0 0 24 23" fill="none" stroke="#4a4e55" stroke-width="2.5"><path d="m12 1 3.3 7 7.7.9-5.7 5.3 1.5 7.6L12 18l-6.8 3.8 1.5-7.6L1 8.9 8.7 8z"/></svg>4.5</span></div>
  </article>

  <!-- row 2 -->
  <article class="card" style="left:277px;top:527px">
    <div class="card-stack"><div class="card-face">
      <svg class="chart" width="273" height="189" viewBox="0 0 273 189">
        <text x="28" y="20" font-size="6" font-weight="600" fill="#222">Right Y-axis</text>
        <text x="28" y="36" font-size="5.5" fill="#777">Population of Largest U.S. Cities</text>
        <text x="28" y="45" font-size="4.5" fill="#aaa">Based on most recent and previous census data</text>
        <g stroke="#e3e3e3" stroke-width=".7"><path d="M100 60v100M172 60v100M244 60v100"/></g>
        <g fill="var(--chart-blue)"><rect x="28" y="67" width="245" height="4"/><rect x="28" y="89" width="135" height="4"/><rect x="28" y="106" width="95" height="4"/><rect x="28" y="123" width="72" height="4"/><rect x="28" y="142" width="53" height="4"/></g>
        <g fill="var(--chart-red)"><rect x="28" y="72" width="245" height="4"/><rect x="28" y="94" width="130" height="4"/><rect x="28" y="111" width="103" height="4"/><rect x="28" y="128" width="65" height="4"/><rect x="28" y="147" width="55" height="4"/></g>
        <path d="M28 60v100" stroke="#999" stroke-width=".8"/>
        <g font-size="4.5" fill="#666"><text x="26" y="168">0</text><text x="96" y="168">2M</text><text x="168" y="168">4M</text><text x="240" y="168">6M</text></g>
      </svg>
    </div></div>
    <h3 class="card-title">Bar Charts Lorem Ipsum</h3>
    <div class="card-meta"><span>12 VIEW</span><span>I</span><span><svg width="10" height="10" viewBox="0 0 24 23" fill="none" stroke="#4a4e55" stroke-width="2.5"><path d="m12 1 3.3 7 7.7.9-5.7 5.3 1.5 7.6L12 18l-6.8 3.8 1.5-7.6L1 8.9 8.7 8z"/></svg>4.5</span></div>
  </article>

  <article class="card" style="left:577px;top:527px">
    <div class="card-stack"><div class="card-face">
      <svg class="chart" width="273" height="189" viewBox="0 0 273 189">
        <text x="70" y="31" font-size="5.5" fill="#222">My Daily Activities</text>
        <path d="M135 96V41A55 55 0 0 1 150.3 148.8Z" fill="var(--chart-blue)"/>
        <path d="M135 96 150.3 148.8A55 55 0 0 1 119.3 148.7Z" fill="var(--chart-red)"/>
        <path d="M135 96 119.3 148.7A55 55 0 0 1 93.3 131.8Z" fill="var(--chart-orange)"/>
        <path d="M135 96 93.3 131.8A55 55 0 0 1 80.5 103.5Z" fill="var(--chart-green)"/>
        <path d="M135 96 80.5 103.5A55 55 0 0 1 135 41Z" fill="var(--chart-purple)"/>
        <g font-size="4.5" fill="#fff"><text x="163" y="96">45.5%</text><text x="90" y="76">27.3%</text><text x="129" y="141">9.1%</text><text x="103" y="134">9.1%</text><text x="90" y="117">9.1%</text></g>
        <g font-size="4.5" fill="#444">
          <circle cx="211" cy="45" r="2" fill="var(--chart-blue)"/><text x="216" y="47">Work</text>
          <circle cx="211" cy="54" r="2" fill="var(--chart-red)"/><text x="216" y="56">Eat</text>
          <circle cx="211" cy="63" r="2" fill="var(--chart-orange)"/><text x="216" y="65">Commute</text>
          <circle cx="211" cy="72" r="2" fill="var(--chart-green)"/><text x="216" y="74">Watch TV</text>
          <circle cx="211" cy="81" r="2" fill="var(--chart-purple)"/><text x="216" y="83">Sleep</text>
        </g>
      </svg>
    </div></div>
    <h3 class="card-title">Visualization: Pie Chart</h3>
    <div class="card-meta"><span>12 VIEW</span><span>I</span><span><svg width="10" height="10" viewBox="0 0 24 23" fill="none" stroke="#4a4e55" stroke-width="2.5"><path d="m12 1 3.3 7 7.7.9-5.7 5.3 1.5 7.6L12 18l-6.8 3.8 1.5-7.6L1 8.9 8.7 8z"/></svg>4.5</span></div>
  </article>

  <article class="card" style="left:877px;top:527px">
    <div class="card-stack"><div class="card-face">
      <svg class="chart" width="273" height="189" viewBox="0 0 273 189">
        <text x="52" y="30" font-size="4.5" fill="#222">Correlation between life expectancy, fertility rate</text>
        <text x="52" y="36" font-size="4.5" fill="#222">and population of some world countries (2010)</text>
        <g stroke="#e3e3e3" stroke-width=".7"><path d="M52 43h161M52 75h161M52 107h161M52 140h161M92 43v97M132 43v97M172 43v97M213 43v97"/></g>
        <circle cx="72" cy="70" r="3" fill="var(--chart-orange)"/>
        <circle cx="73" cy="98" r="4.5" fill="var(--chart-orange)" stroke="#fff" stroke-width=".6"/>
        <circle cx="92" cy="98" r="6" fill="var(--chart-red)" stroke="#fff" stroke-width=".6"/>
        <circle cx="117" cy="89" r="5" fill="var(--chart-orange)" stroke="#fff" stroke-width=".6"/>
        <circle cx="117" cy="101" r="4" fill="var(--chart-orange)" stroke="#fff" stroke-width=".6"/>
        <circle cx="155" cy="96" r="8" fill="var(--chart-blue)" stroke="#fff" stroke-width=".6"/>
        <circle cx="174" cy="97" r="4" fill="var(--chart-red)" stroke="#fff" stroke-width=".6"/>
        <circle cx="175" cy="105" r="4" fill="var(--chart-red)" stroke="#fff" stroke-width=".6"/>
        <circle cx="181" cy="86" r="2" fill="var(--chart-orange)"/>
        <g font-size="4" fill="#444">
          <rect x="218" y="46" width="4" height="4" fill="var(--chart-blue)"/><text x="224" y="50">North</text>
          <rect x="218" y="53" width="4" height="4" fill="var(--chart-red)"/><text x="224" y="57">Europe</text>
          <rect x="218" y="60" width="4" height="4" fill="var(--chart-orange)"/><text x="224" y="64">Middle</text>
        </g>
        <g font-size="4" fill="#666"><text x="45" y="46">3.5</text><text x="45" y="78">2.5</text><text x="45" y="110">1.5</text><text x="118" y="156">Life Expectancy</text><text x="40" y="100" transform="rotate(-90 40 100)">Fertility</text></g>
      </svg>
    </div></div>
    <h3 class="card-title">Visualization: Bubble Chart</h3>
    <div class="card-meta"><span>12 VIEW</span><span>I</span><span><svg width="10" height="10" viewBox="0 0 24 23" fill="none" stroke="#4a4e55" stroke-width="2.5"><path d="m12 1 3.3 7 7.7.9-5.7 5.3 1.5 7.6L12 18l-6.8 3.8 1.5-7.6L1 8.9 8.7 8z"/></svg>4.5</span></div>
  </article>
</main>

</body>
</html>
```